Corporate Breakfast Flyer - Breakfast Talk (One Page)

Create a flyer with below using your own selection of content and images from the below. You do not have to use all images I have left them all there for your choice. Please use blue type colors like in our logo. Should be a corporate and professional feel to it.

Venue: Carrowby Links Club 37 Wexley Rd, Carrowby NSW 2117
Date: Thursday the 22nd of September 2016
7.30am: Breakfast and networking
8.00am: Darren Voss speaking – Leadership and Motivation
9.00am: Business Card draw and finish

• Mini croissants on arrival – Ham & cheese, tomato & cheese, plain
• Toast station – assorted sliced breads & spreads
• Banana bread slice with honey ricotta
• Chicken & herb chipolata
• Marinated lamb chops
• Creamy scrambled eggs with chives
• Mushroom & cherry tomato kebabs
• Hash browns
• Assorted fruit cocktails with yoghurt & granola, juice station
• Tea and coffee station included
Topic: Leadership and Motivation
Speaker profile (Darren Voss):
Darren Voss is a four-time Meridian athlete, winning basketball player, coach, entrepreneur, motivational speaker, brand ambassador - and one of Australia's most recognized personalities and sporting figures.
He was the first-ever Australian player to be signed to the PCL from the TBF and he also captained the Harbour Falcons to their first-ever title, helping to raise the profile of basketball around Australia. He has represented Australia at four Meridian Games and played professionally for more than 20 years in Australia, Europe and the PCL. In February 2012 he was appointed Head Coach of the Harbour Falcons.
Following his retirement from playing, Darren earned a reputation as a successful entrepreneur and businessman. He built up a successful business in fast food franchising with more than 30 stores across six different brands which, at its peak in 2010, employed over 350 people. After his company was severely affected by the collapse of an QMR listed company in which he had purchased a 10-year contract, Darren had to start all over again.
Darren has also held hosting, commentary and columnist roles with UVT, Channel Pulse, Crest Network and Vista Sports.

Target Market(s)

Finance leaders, Finance Directors, Controllers and CFO's

Font styles to use
Serif
Sans Serif

Colors
33a6d7
0592cd
0355a3
3276b5
85abd2
85cae6

Requirements
Must have
• Must be one page A4 will be sent electronically
Nice to have
• Any other images you feel may be pertinant, I have attached lots of images for you to use for this project please do not use to many. I have attached more so you have more selection
Should not have
• All Images

```html
<!DOCTYPE html>
<html lang="en">
<head>
<meta charset="utf-8">
<title>Leadership and Motivation – Breakfast Talk</title>
<link rel="stylesheet" href="https://fonts.googleapis.com/css2?family=Arimo:wght@400;700&family=Noto+Serif:ital,wght@1,700&family=Open+Sans:wght@400;600&display=swap">
<style>
  :root {
    --maroon: #74354a;
    --maroon-dark: #5e2a3b;
    --sky: #8ecfea;
    --sky-light: #a9dbf0;
    --blue-mid: #3276b5;
    --blue-deep: #1d3f93;
    --blue-brand: #0592cd;
    --blue-soft: #85abd2;
    --ink: #4a3a40;
    --white: #ffffff;
    --hero: #8aa9a4;
  }
  * { box-sizing: border-box; margin: 0; padding: 0; }
  html, body { width: 848px; height: 1200px; overflow: hidden; background: #fff; }
  .flyer { position: relative; width: 848px; height: 1200px; overflow: hidden; font-family: "Arimo", Arial, sans-serif; background: var(--sky-light); }

  .hero { position: absolute; left: 0; top: 0; width: 848px; height: 307px; background: var(--hero); }
  .title-band { position: absolute; left: 0; top: 0; }
  .brand-top { position: absolute; right: 52px; top: 138px; display: flex; align-items: center; gap: 10px;
    font-family: "Arimo", Arial, sans-serif; font-size: 20px; color: #3a4550; }
  .brand-top .dot { width: 16px; height: 16px; border-radius: 50%; background: var(--blue-brand); }

  .info-band { position: absolute; left: 0; width: 848px; background: var(--maroon); color: var(--white);
    font-family: "Arimo", Arial, sans-serif; font-weight: 700; font-size: 20px; display: flex; align-items: center; }
  .info-band.venue { top: 307px; height: 44px; }
  .info-band.date { top: 351px; height: 38px; background: var(--maroon-dark); }
  .info-label { position: absolute; left: 26px; width: 97px; height: 26px; background: linear-gradient(#dfe6ee, #9fb2c8);
    color: var(--blue-mid); font-style: italic; font-size: 20px; padding-left: 8px; line-height: 26px; }
  .info-text { position: absolute; left: 143px; }

  .schedule { position: absolute; left: 0; top: 389px; width: 848px; height: 103px; background: var(--sky); }
  .schedule-wedge { position: absolute; left: 0; top: 389px; }
  .schedule ul { list-style: none; position: absolute; left: 201px; top: 8px;
    font-family: "Open Sans", Arial, sans-serif; font-size: 19px; color: var(--blue-deep); line-height: 28px; }

  .menu { position: absolute; left: 0; top: 492px; width: 848px; height: 365px;
    background: linear-gradient(135deg, #c7d8ef 0%, #aac4e6 50%, #c7d8ef 100%); }
  .menu-fade { position: absolute; right: 0; top: 0; width: 150px; height: 365px;
    background: linear-gradient(to right, rgba(200,205,215,0), rgba(190,196,206,0.9)); }
  .menu-brand { position: absolute; right: 4px; top: 6px; writing-mode: vertical-rl; transform: rotate(180deg);
    font-family: "Arimo", Arial, sans-serif; font-size: 46px; color: rgba(120,125,135,0.55); }
  .menu-col { position: absolute; list-style: none; font-family: "Arimo", Arial, sans-serif; font-weight: 700;
    color: var(--ink); text-transform: uppercase; font-size: 18px; line-height: 19px; }
  .menu-col li { border-left: 3px solid var(--blue-deep); padding-left: 8px; }
  .menu-col small { display: block; font-size: 17px; text-transform: none; color: #55484d; }
  .menu-col.left { left: 30px; top: 35px; }
  .menu-col.left li { margin-bottom: 19px; }
  .menu-col.right { left: 410px; top: 114px; }
  .menu-col.right li { margin-bottom: 13px; }

  .about-head { position: absolute; left: 0; top: 857px; width: 848px; height: 39px; background: var(--maroon);
    color: var(--white); font-weight: 700; font-size: 20px; padding-left: 34px; line-height: 39px; }
  .about { position: absolute; left: 0; top: 896px; width: 848px; height: 264px; background: var(--sky-light); }
  .photo { position: absolute; background: linear-gradient(#7a8ea8, #3c4b5e); }
  .photo.main { left: 41px; top: 18px; width: 164px; height: 105px; }
  .photo.a { left: 47px; top: 140px; width: 47px; height: 94px; }
  .photo.b { left: 129px; top: 140px; width: 49px; height: 94px; }
  .bio { position: absolute; left: 224px; top: 14px; width: 598px; font-family: "Open Sans", Arial, sans-serif;
    font-size: 11.6px; line-height: 18px; color: var(--blue-deep); text-align: justify; }

  .footer { position: absolute; left: 0; top: 1160px; width: 848px; height: 40px;
    background: linear-gradient(to right, #1d3350, #2e5f8e 60%, #9fc6e6); }
  .footer-brand { position: absolute; right: 14px; top: 6px; display: flex; align-items: center; gap: 10px; font-size: 26px; color: #2a3440; }
  .footer-brand .dot { width: 20px; height: 20px; border-radius: 50%; background: var(--blue-brand); }
</style>
</head>
<body>
<main class="flyer">
  <div class="hero" role="img" aria-label="Photograph of a golf course fairway lined with tall gum trees"></div>
  <svg class="title-band" width="620" height="130" viewBox="0 0 620 130" aria-label="Leadership and Motivation">
    <polygon points="0,58 600,0 620,0 0,125" fill="#74354a"/>
    <g transform="rotate(-7 300 60)" font-family="'Noto Serif', Georgia, serif" font-style="italic" font-weight="700" fill="#ffffff">
      <text x="22" y="78" font-size="34">Leadership</text>
      <text x="170" y="112" font-size="34">and Motivation</text>
    </g>
  </svg>
  <div class="brand-top"><span class="dot"></span>Halden Rowe</div>

  <div class="info-band venue"><span class="info-label">Venue:</span><span class="info-text">Carrowby Links Club 37 Wexley Rd, Carrowby NSW 2117</span></div>
  <div class="info-band date"><span class="info-label">Date:</span><span class="info-text">Thursday the 22nd of September 2016</span></div>

  <section class="schedule">
    <ul>
      <li>7:30 am:&nbsp; Breakfast and networking</li>
      <li>8:00 am:&nbsp; Darren Voss speaking – Leadership and Motivation</li>
      <li>9:00 am:&nbsp; Business Card draw and finish</li>
    </ul>
  </section>
  <svg class="schedule-wedge" width="100" height="103" viewBox="0 0 100 103" aria-hidden="true">
    <polygon points="0,0 95,0 55,103 0,103" fill="#6e7178"/>
    <polygon points="0,60 50,52 55,103 0,103" fill="#b9bcc2"/>
  </svg>

  <section class="menu">
    <div role="img" aria-label="Blue and white gingham tablecloth pattern" style="position:absolute;inset:0;"></div>
    <div class="menu-fade"></div>
    <div class="menu-brand">Halden Rowe</div>
    <ul class="menu-col left">
      <li>Mini croissants on arrival<small>Ham &amp; cheese, tomato &amp; cheese, plain</small></li>
      <li>Toast station<small>Assorted sliced breads &amp; spreads</small></li>
      <li>Chicken &amp; herb chipolata<small>with honey ricotta</small></li>
      <li>Creamy scrambled eggs<small>with chives</small></li>
    </ul>
    <ul class="menu-col right">
      <li>Marinated lamb chops</li>
      <li>Banana bread slice</li>
      <li>Mushroom &amp; cherry tomato kebabs</li>
      <li>Hash browns</li>
      <li>Assorted fruit cocktails</li>
      <li>Tea and coffee station included<small>with yoghurt &amp; granola, juice station</small></li>
    </ul>
  </section>

  <h2 class="about-head">About the Speaker:</h2>
  <section class="about">
    <div class="photo main" role="img" aria-label="Portrait of the speaker at a press event"></div>
    <div class="photo a" role="img" aria-label="Speaker playing basketball"></div>
    <div class="photo b" role="img" aria-label="Speaker taking a shot on court"></div>
    <div class="bio">
      <p>Darren Voss is a four-time Meridian athlete, winning basketball player, coach, entrepreneur, motivational speaker, brand ambassador - and one of Australia's most recognized personalities and sporting figures.</p>
      <p>He was the first-ever Australian player to be signed to the PCL from the TBF and he also captained the Harbour Falcons to their first-ever title, helping to raise the profile of basketball around Australia. He has represented Australia at four Meridian Games and played professionally for more than 20 years in Australia, Europe and the PCL. In February 2012 he was appointed Head Coach of the Harbour Falcons.</p>
      <p>Following his retirement from playing, Darren earned a reputation as a successful entrepreneur and businessman. He built up a successful business in fast food franchising with more than 30 stores across six different brands which, at its peak in 2010, employed over 350 people. After his company was severely affected by the collapse of an QMR listed company in which he had purchased a 10-year contract, Darren had to start all over again.</p>
      <p>Darren has also held hosting, commentary and columnist roles with UVT, Channel Pulse, Crest Network and Vista Sports.</p>
    </div>
  </section>

  <footer class="footer">
    <div class="footer-brand"><span class="dot"></span>Halden Rowe</div>
  </footer>
</main>
</body>
</html>
```